7th Annual Falcon Invitational Flyer

Looking to design an updated eye catching flyer maybe with someone movement, sound, and color. Below is an attachment of the flyer I have used in the past. I need to add color, sound, and movement to the flyer. This is an advertisement for youth folk style wrestling. You may contact me directly at 252-381-4926 if you need additional information. I really like the colors music and movement in the video below.
https://www.vidmarlo.com/watch?v=qT4kLmPzw8e

Target Market(s)

Youth Wrestling

Font styles to use
Serif

Colors
EB3D1F
EC4F4E
F09395
F8D3D4
FCEDEE

Requirements
Must have
• All information included on flyer.
Nice to have
• Color, sound, and movement

```html
<!DOCTYPE html>
<html lang="en">
<head>
<meta charset="utf-8">
<title>7th Annual Falcon Invitational – Flyer Variations</title>
<link href="https://fonts.googleapis.com/css2?family=Anton&family=Poppins:ital,wght@0,500;0,600;1,400;1,500&display=swap" rel="stylesheet">
<style>
:root{
  --board:#2a0c10;
  --red-deep:#5c0b0d;
  --red-mid:#9a1513;
  --red-hot:#c4231c;
  --accent:#eb3d1f;
  --accent-soft:#ec4f4e;
  --pink:#f09395;
  --blush:#f8d3d4;
  --cream:#fcedee;
  --panel:rgba(38,6,8,.78);
  --white:#ffffff;
}
*{margin:0;padding:0;box-sizing:border-box}
html,body{width:905px;height:1200px;overflow:hidden;background:var(--board)}
.board{position:relative;width:905px;height:1200px;background:var(--board)}
.flyer{position:absolute;width:702px;height:993px;transform-origin:0 0;transform:scale(.5423);overflow:hidden;
  font-family:"Poppins",sans-serif;color:var(--cream);
  background:radial-gradient(ellipse at 60% 40%,var(--red-hot) 0%,var(--red-mid) 45%,var(--red-deep) 100%)}
.flyer--a{left:54px;top:49px}
.flyer--b{left:471px;top:49px}
.flyer--c{left:54px;top:614px}
.flyer--d{left:471px;top:614px}
.backdrop{position:absolute}
.backdrop--figure{left:150px;top:180px;width:260px;height:700px;border-radius:40% 40% 20% 20%;
  background:radial-gradient(ellipse at 50% 40%,rgba(120,20,16,.55),rgba(90,12,10,0) 70%)}
.backdrop--warrior{left:230px;top:0;width:472px;height:993px;
  background:radial-gradient(ellipse at 40% 12%,rgba(190,150,90,.55),rgba(0,0,0,0) 28%),
  radial-gradient(ellipse at 55% 55%,rgba(200,120,70,.45),rgba(0,0,0,0) 55%)}
.headline{position:absolute;left:62px;top:28px;height:70px;white-space:nowrap}
.headline .num{position:absolute;left:0;top:0;font-family:"Anton",sans-serif;font-size:72px;line-height:1;color:var(--accent);
  font-style:italic;-webkit-text-stroke:2px var(--white)}
.headline .sup{position:absolute;left:48px;top:4px;font-family:"Anton",sans-serif;font-size:16px;color:var(--white)}
.headline .title{position:absolute;left:46px;top:26px;font-family:"Anton",sans-serif;font-size:37px;line-height:1;letter-spacing:.3px;
  color:var(--accent);-webkit-text-stroke:1.4px var(--white);text-shadow:2px 2px 0 var(--red-deep)}
.label{position:absolute;background:var(--accent);color:var(--white);font-weight:600;font-size:12.5px;line-height:16px;padding:0 7px}
.line{position:absolute;font-style:italic;font-size:13px;line-height:17px;white-space:nowrap}
.bar{position:absolute;background:var(--accent);color:var(--white);font-weight:600;font-size:12.5px;line-height:21px;text-align:center}
.panel{position:absolute;background:var(--panel);font-style:italic;font-size:12.5px;line-height:17px;text-align:center;padding-top:2px}
.panel--left{text-align:left;padding-left:6px;font-size:13px;line-height:18.5px}
.org{position:absolute;text-align:center;font-family:"Poppins",sans-serif;font-weight:600;color:var(--white)}
.org .mark{display:block;width:84px;height:58px;margin:6px auto;border-radius:50%;background:var(--white)}
.org .name{font-size:17px;line-height:18px}
.org .tag{font-size:8.5px;line-height:11px}
.helmet{position:absolute;left:512px;top:95px;width:156px;height:280px;border-radius:70px 70px 20px 20px;
  background:linear-gradient(180deg,#2b2224,#0f0a0b)}
.helmet-name{position:absolute;left:512px;top:128px;width:156px;text-align:center;font-weight:600;font-size:13px;color:var(--white)}
.divisions{position:absolute;border:2px solid var(--blush);border-collapse:collapse;background:var(--panel)}
.divisions td{border:1px solid var(--blush);font-size:12.5px;padding:0 5px;vertical-align:middle}
.divisions td.weights{font-style:italic;font-size:10.5px;line-height:12px}
.divisions--boys{left:38px;top:397px;width:308px}
.divisions--boys tr{height:28.5px}
.divisions--boys td:first-child{width:96px;font-style:italic}
.divisions--girls{left:360px;top:397px;width:310px}
.divisions--girls tr{height:36px}
.divisions--girls td:first-child{width:98px;font-style:italic}
.notes{position:absolute;left:0;width:702px;top:755px;text-align:center;font-style:italic;font-size:12.8px;line-height:17px}
.footer-left{position:absolute;left:34px;top:896px;font-weight:600;font-size:11.5px;line-height:16.5px}
.footer-left .phone{letter-spacing:2px}
.footer-right{position:absolute;left:477px;top:893px;font-style:italic;font-size:13px;line-height:17.5px}
</style>
</head>
<body>
<main class="board">

<!-- Variation A -->
<section class="flyer flyer--a">
  <div class="backdrop backdrop--figure" role="img" aria-label="Faint photograph of a warrior figure in the red textured background"></div>
  <div class="headline"><span class="num">7</span><span class="sup">TH</span><span class="title">ANNUAL FALCON INVITATIONAL</span></div>
  <span class="label" style="left:40px;top:108px">Date:</span>
  <p class="line" style="left:42px;top:126px">Saturday, January 25, 2025</p>
  <span class="label" style="left:342px;top:108px">Location:</span>
  <p class="line" style="left:344px;top:126px">Riverside Expo Center<br>512 Oakmont Blvd SW<br>Greenville, NC 27834</p>
  <div class="org" style="left:522px;top:118px;width:170px"><span class="name">ECYWA</span><span class="mark"></span><span class="tag">EASTERN CAROLINA YOUTH<br>WRESTLING ALLIANCE</span></div>
  <span class="label" style="left:40px;top:177px">Time:</span>
  <p class="line" style="left:42px;top:195px">4U, 6U, 8U, 10U – Wrestling Starts at 8:30 am<br>12U, Middle School, &amp; High School – Wrestling Starts at 1:00 pm</p>
  <div class="bar" style="left:197px;top:242px;width:306px">Register @ www.matbracket.com</div>
  <div class="panel" style="left:85px;top:270px;width:485px;height:87px">Early Registration $30.00 Deadline is January 19, 2025 at 11:59PM<br>Regular Registration $40.00 Deadline is January 22, 2025 at 11:59PM<br>Late Registration $50.00 Deadline is January 24, 2025 at 5:00PM<br>Registration is limited to the first 500 wrestlers<br>Non-ECYWA Card Holders will pay an additional $5.00 at weigh-ins.</div>
  <span class="label" style="left:38px;top:369px">Boys Divisions:</span>
  <table class="divisions divisions--boys">
    <tr><td>4 &amp; Under</td><td class="weights">30, 40, 50, HWT</td></tr>
    <tr><td>6 &amp; Under</td><td class="weights">36, 40, 44, 48, 52, 56, 60, HWT</td></tr>
    <tr><td>8 &amp; Under</td><td class="weights">40,44,48,52,56,60,64,68,72,<br>76,80,84,88,92, HWT</td></tr>
    <tr><td>10 &amp; Under</td><td class="weights">52,56,60,64,68,72,76,80,84,<br>88,92,96,100,110, HWT</td></tr>
    <tr><td>12 &amp; Under</td><td class="weights">64,68,72,76,80,84,88,92,96,100,<br>105,110,115,120,130,140,160, HWT</td></tr>
    <tr><td>Middle School</td><td class="weights">72,76,80,88,92,96,100,105,110,115,<br>120,130,140,160,210, HWT</td></tr>
    <tr><td>High School</td><td class="weights">106,113,120,126,132,138,144,150,157,<br>165,175,190,215, HWT</td></tr>
  </table>
  <span class="label" style="left:358px;top:369px">Girls Divisions:</span>
  <table class="divisions divisions--girls">
    <tr><td>K - 5</td><td class="weights">36,40,44,48,52,56,60,64,68,72,76,<br>80,84,88,92,96,100,110,120,HWT</td></tr>
    <tr><td>Middle School</td><td class="weights">72,76,83,90,98,106,113,120,126,132,138,<br>145,152,160,170,182,190,220, HWT</td></tr>
    <tr><td>Women's<br>High School</td><td class="weights">100,107,114,120,126,132,145,152,165,<br>185, HWT</td></tr>
  </table>
  <div class="panel" style="left:78px;top:612px;width:546px;height:38px">*Age is based upon wrestler's age as of December 31, 2024.<br>Tournament director has the right to combine weight classes if deemed necessary.</div>
  <span class="label" style="left:38px;top:664px">Weigh-ins:</span>
  <div class="panel panel--left" style="left:38px;top:690px;width:560px;height:60px">January 24, 2025 – 5:00 pm to 7:00 pm (Early Weigh-ins - $10 cash due at scale)<br>January 25, 2025 – 6:00 am to 7:30 am (4U, 6U, 8U, 10U)<br>January 25, 2025 – 11:00 am to 12:00 pm (12 &amp; Under, MS, &amp; High School)</div>
  <p class="notes">Tenths are waived/dropped at weigh-ins. Satellite weigh-ins will not be allowed.<br>High School Divisions are given 2 lbs. growth allowance.<br>Custom medals will be given to the top 3 individual finishers in each bracket.<br>Custom Awards will be awarded to the top 4 teams. Referee decisions will be final.<br>Pamlico Sound Athletics is not responsible for accidents, injuries, or theft during the tournament.</p>
  <div class="bar" style="left:196px;top:855px;width:310px">Admission: $10.00 per person</div>
  <p class="footer-left">For More Information,<br>contact Tournament Director Dale Haskins:<br><span class="phone">252-381-4926</span></p>
  <p class="footer-right">Hotels Available On-Site<br>Lakeview Suites (252)318-4100<br>Maple Lodge Inn (252)318-6200<br>Harborside Inn (252)318-7300</p>
</section>

<!-- Variation B -->
<section class="flyer flyer--b">
  <div class="backdrop backdrop--warrior" role="img" aria-label="Photograph of a shouting helmeted warrior with a bare muscular torso"></div>
  <div class="headline"><span class="num">7</span><span class="sup">TH</span><span class="title">ANNUAL FALCON INVITATIONAL</span></div>
  <span class="label" style="left:40px;top:108px">Date:</span>
  <p class="line" style="left:42px;top:126px">Saturday, January 25, 2025</p>
  <span class="label" style="left:342px;top:108px">Location:</span>
  <p class="line" style="left:344px;top:126px">Riverside Expo Center<br>512 Oakmont Blvd SW<br>Greenville, NC 27834</p>
  <div class="org" style="left:522px;top:118px;width:170px"><span class="name">ECYWA</span><span class="mark"></span><span class="tag">EASTERN CAROLINA YOUTH<br>WRESTLING ALLIANCE</span></div>
  <span class="label" style="left:40px;top:177px">Time:</span>
  <p class="line" style="left:42px;top:195px">4U, 6U, 8U, 10U – Wrestling Starts at 8:30 am<br>12U, Middle School, &amp; High School – Wrestling Starts at 1:00 pm</p>
  <div class="bar" style="left:197px;top:242px;width:306px">Register @ www.matbracket.com</div>
  <div class="panel" style="left:85px;top:270px;width:485px;height:87px">Early Registration $30.00 Deadline is January 19, 2025 at 11:59PM<br>Regular Registration $40.00 Deadline is January 22, 2025 at 11:59PM<br>Late Registration $50.00 Deadline is January 24, 2025 at 5:00PM<br>Registration is limited to the first 500 wrestlers<br>Non-ECYWA Card Holders will pay an additional $5.00 at weigh-ins.</div>
  <span class="label" style="left:38px;top:369px">Boys Divisions:</span>
  <table class="divisions divisions--boys">
    <tr><td>4 &amp; Under</td><td class="weights">30, 40, 50, HWT</td></tr>
    <tr><td>6 &amp; Under</td><td class="weights">36, 40, 44, 48, 52, 56, 60, HWT</td></tr>
    <tr><td>8 &amp; Under</td><td class="weights">40,44,48,52,56,60,64,68,72,<br>76,80,84,88,92, HWT</td></tr>
    <tr><td>10 &amp; Under</td><td class="weights">52,56,60,64,68,72,76,80,84,<br>88,92,96,100,110, HWT</td></tr>
    <tr><td>12 &amp; Under</td><td class="weights">64,68,72,76,80,84,88,92,96,100,<br>105,110,115,120,130,140,160, HWT</td></tr>
    <tr><td>Middle School</td><td class="weights">72,76,80,88,92,96,100,105,110,115,<br>120,130,140,160,210, HWT</td></tr>
    <tr><td>High School</td><td class="weights">106,113,120,126,132,138,144,150,157,<br>165,175,190,215, HWT</td></tr>
  </table>
  <span class="label" style="left:358px;top:369px">Girls Divisions:</span>
  <table class="divisions divisions--girls">
    <tr><td>K - 5</td><td class="weights">36,40,44,48,52,56,60,64,68,72,76,<br>80,84,88,92,96,100,110,120,HWT</td></tr>
    <tr><td>Middle School</td><td class="weights">72,76,83,90,98,106,113,120,126,132,138,<br>145,152,160,170,182,190,220, HWT</td></tr>
    <tr><td>Women's<br>High School</td><td class="weights">100,107,114,120,126,132,145,152,165,<br>185, HWT</td></tr>
  </table>
  <div class="panel" style="left:78px;top:612px;width:546px;height:38px">*Age is based upon wrestler's age as of December 31, 2024.<br>Tournament director has the right to combine weight classes if deemed necessary.</div>
  <span class="label" style="left:38px;top:664px">Weigh-ins:</span>
  <div class="panel panel--left" style="left:38px;top:690px;width:560px;height:60px">January 24, 2025 – 5:00 pm to 7:00 pm (Early Weigh-ins - $10 cash due at scale)<br>January 25, 2025 – 6:00 am to 7:30 am (4U, 6U, 8U, 10U)<br>January 25, 2025 – 11:00 am to 12:00 pm (12 &amp; Under, MS, &amp; High School)</div>
  <p class="notes">Tenths are waived/dropped at weigh-ins. Satellite weigh-ins will not be allowed.<br>High School Divisions are given 2 lbs. growth allowance.<br>Custom medals will be given to the top 3 individual finishers in each bracket.<br>Custom Awards will be awarded to the top 4 teams. Referee decisions will be final.<br>Pamlico Sound Athletics is not responsible for accidents, injuries, or theft during the tournament.</p>
  <div class="bar" style="left:196px;top:855px;width:310px">Admission: $10.00 per person</div>
  <p class="footer-left">For More Information,<br>contact Tournament Director Dale Haskins:<br><span class="phone">252-381-4926</span></p>
  <p class="footer-right">Hotels Available On-Site<br>Lakeview Suites (252)318-4100<br>Maple Lodge Inn (252)318-6200<br>Harborside Inn (252)318-7300</p>
</section>

<!-- Variation C -->
<section class="flyer flyer--c">
  <div class="backdrop backdrop--figure" role="img" aria-label="Faint photograph of a warrior figure in the red textured background"></div>
  <div class="headline"><span class="num">7</span><span class="sup">TH</span><span class="title">ANNUAL FALCON INVITATIONAL</span></div>
  <span class="label" style="left:40px;top:108px">Date:</span>
  <p class="line" style="left:42px;top:126px">Saturday, January 25, 2025</p>
  <span class="label" style="left:296px;top:108px">Location:</span>
  <p class="line" style="left:298px;top:126px">Riverside Expo Center<br>512 Oakmont Blvd SW<br>Greenville, NC 27834</p>
  <div class="helmet" role="img" aria-label="Illustration of a black warrior helmet"></div>
  <p class="helmet-name">ECYWA</p>
  <span class="label" style="left:40px;top:177px">Time:</span>
  <p class="line" style="left:42px;top:195px">4U, 6U, 8U, 10U – Wrestling Starts at 8:30 am<br>12U, Middle School, &amp; High School – Wrestling Starts at 1:00 pm</p>
  <div class="bar" style="left:130px;top:242px;width:306px">Register @ www.matbracket.com</div>
  <div class="panel" style="left:68px;top:270px;width:448px;height:87px">Early Registration $30.00 Deadline is January 19, 2025 at 11:59PM<br>Regular Registration $40.00 Deadline is January 22, 2025 at 11:59PM<br>Late Registration $50.00 Deadline is January 24, 2025 at 5:00PM<br>Registration is limited to the first 500 wrestlers<br>Non-ECYWA Card Holders will pay an additional $5.00 at weigh-ins.</div>
  <span class="label" style="left:38px;top:369px">Boys Divisions:</span>
  <table class="divisions divisions--boys">
    <tr><td>4 &amp; Under</td><td class="weights">30, 40, 50, HWT</td></tr>
    <tr><td>6 &amp; Under</td><td class="weights">36, 40, 44, 48, 52, 56, 60, HWT</td></tr>
    <tr><td>8 &amp; Under</td><td class="weights">40,44,48,52,56,60,64,68,72,<br>76,80,84,88,92, HWT</td></tr>
    <tr><td>10 &amp; Under</td><td class="weights">52,56,60,64,68,72,76,80,84,<br>88,92,96,100,110, HWT</td></tr>
    <tr><td>12 &amp; Under</td><td class="weights">64,68,72,76,80,84,88,92,96,100,<br>105,110,115,120,130,140,160, HWT</td></tr>
    <tr><td>Middle School</td><td class="weights">72,76,80,88,92,96,100,105,110,115,<br>120,130,140,160,210, HWT</td></tr>
    <tr><td>High School</td><td class="weights">106,113,120,126,132,138,144,150,157,<br>165,175,190,215, HWT</td></tr>
  </table>
  <span class="label" style="left:358px;top:369px">Girls Divisions:</span>
  <table class="divisions divisions--girls">
    <tr><td>K - 5</td><td class="weights">36,40,44,48,52,56,60,64,68,72,76,<br>80,84,88,92,96,100,110,120,HWT</td></tr>
    <tr><td>Middle School</td><td class="weights">72,76,83,90,98,106,113,120,126,132,138,<br>145,152,160,170,182,190,220, HWT</td></tr>
    <tr><td>Women's<br>High School</td><td class="weights">100,107,114,120,126,132,145,152,165,<br>185, HWT</td></tr>
  </table>
  <div class="panel" style="left:78px;top:612px;width:546px;height:38px">*Age is based upon wrestler's age as of December 31, 2024.<br>Tournament director has the right to combine weight classes if deemed necessary.</div>
  <span class="label" style="left:38px;top:664px">Weigh-ins:</span>
  <div class="panel panel--left" style="left:38px;top:690px;width:560px;height:60px">January 24, 2025 – 5:00 pm to 7:00 pm (Early Weigh-ins - $10 cash due at scale)<br>January 25, 2025 – 6:00 am to 7:30 am (4U, 6U, 8U, 10U)<br>January 25, 2025 – 11:00 am to 12:00 pm (12 &amp; Under, MS, &amp; High School)</div>
  <p class="notes">Tenths are waived/dropped at weigh-ins. Satellite weigh-ins will not be allowed.<br>High School Divisions are given 2 lbs. growth allowance.<br>Custom medals will be given to the top 3 individual finishers in each bracket.<br>Custom Awards will be awarded to the top 4 teams. Referee decisions will be final.<br>Pamlico Sound Athletics is not responsible for accidents, injuries, or theft during the tournament.</p>
  <div class="bar" style="left:196px;top:855px;width:310px">Admission: $10.00 per person</div>
  <p class="footer-left">For More Information,<br>contact Tournament Director Dale Haskins:<br><span class="phone">252-381-4926</span></p>
  <p class="footer-right">Hotels Available On-Site<br>Lakeview Suites (252)318-4100<br>Maple Lodge Inn (252)318-6200<br>Harborside Inn (252)318-7300</p>
</section>

<!-- Variation D -->
<section class="flyer flyer--d">
  <div class="backdrop backdrop--warrior" role="img" aria-label="Photograph of a shouting helmeted warrior with a bare muscular torso"></div>
  <div class="headline"><span class="num">7</span><span class="sup">TH</span><span class="title">ANNUAL FALCON INVITATIONAL</span></div>
  <span class="label" style="left:40px;top:108px">Date:</span>
  <p class="line" style="left:42px;top:126px">Saturday, January 25, 2025</p>
  <span class="label" style="left:296px;top:108px">Location:</span>
  <p class="line" style="left:298px;top:126px">Riverside Expo Center<br>512 Oakmont Blvd SW<br>Greenville, NC 27834</p>
  <div class="helmet" role="img" aria-label="Illustration of a black warrior helmet"></div>
  <p class="helmet-name">ECYWA</p>
  <span class="label" style="left:40px;top:177px">Time:</span>
  <p class="line" style="left:42px;top:195px">4U, 6U, 8U, 10U – Wrestling Starts at 8:30 am<br>12U, Middle School, &amp; High School – Wrestling Starts at 1:00 pm</p>
  <div class="bar" style="left:130px;top:242px;width:306px">Register @ www.matbracket.com</div>
  <div class="panel" style="left:68px;top:270px;width:448px;height:87px">Early Registration $30.00 Deadline is January 19, 2025 at 11:59PM<br>Regular Registration $40.00 Deadline is January 22, 2025 at 11:59PM<br>Late Registration $50.00 Deadline is January 24, 2025 at 5:00PM<br>Registration is limited to the first 500 wrestlers<br>Non-ECYWA Card Holders will pay an additional $5.00 at weigh-ins.</div>
  <span class="label" style="left:38px;top:369px">Boys Divisions:</span>
  <table class="divisions divisions--boys">
    <tr><td>4 &amp; Under</td><td class="weights">30, 40, 50, HWT</td></tr>
    <tr><td>6 &amp; Under</td><td class="weights">36, 40, 44, 48, 52, 56, 60, HWT</td></tr>
    <tr><td>8 &amp; Under</td><td class="weights">40,44,48,52,56,60,64,68,72,<br>76,80,84,88,92, HWT</td></tr>
    <tr><td>10 &amp; Under</td><td class="weights">52,56,60,64,68,72,76,80,84,<br>88,92,96,100,110, HWT</td></tr>
    <tr><td>12 &amp; Under</td><td class="weights">64,68,72,76,80,84,88,92,96,100,<br>105,110,115,120,130,140,160, HWT</td></tr>
    <tr><td>Middle School</td><td class="weights">72,76,80,88,92,96,100,105,110,115,<br>120,130,140,160,210, HWT</td></tr>
    <tr><td>High School</td><td class="weights">106,113,120,126,132,138,144,150,157,<br>165,175,190,215, HWT</td></tr>
  </table>
  <span class="label" style="left:358px;top:369px">Girls Divisions:</span>
  <table class="divisions divisions--girls">
    <tr><td>K - 5</td><td class="weights">36,40,44,48,52,56,60,64,68,72,76,<br>80,84,88,92,96,100,110,120,HWT</td></tr>
    <tr><td>Middle School</td><td class="weights">72,76,83,90,98,106,113,120,126,132,138,<br>145,152,160,170,182,190,220, HWT</td></tr>
    <tr><td>Women's<br>High School</td><td class="weights">100,107,114,120,126,132,145,152,165,<br>185, HWT</td></tr>
  </table>
  <div class="panel" style="left:78px;top:612px;width:546px;height:38px">*Age is based upon wrestler's age as of December 31, 2024.<br>Tournament director has the right to combine weight classes if deemed necessary.</div>
  <span class="label" style="left:38px;top:664px">Weigh-ins:</span>
  <div class="panel panel--left" style="left:38px;top:690px;width:560px;height:60px">January 24, 2025 – 5:00 pm to 7:00 pm (Early Weigh-ins - $10 cash due at scale)<br>January 25, 2025 – 6:00 am to 7:30 am (4U, 6U, 8U, 10U)<br>January 25, 2025 – 11:00 am to 12:00 pm (12 &amp; Under, MS, &amp; High School)</div>
  <p class="notes">Tenths are waived/dropped at weigh-ins. Satellite weigh-ins will not be allowed.<br>High School Divisions are given 2 lbs. growth allowance.<br>Custom medals will be given to the top 3 individual finishers in each bracket.<br>Custom Awards will be awarded to the top 4 teams. Referee decisions will be final.<br>Pamlico Sound Athletics is not responsible for accidents, injuries, or theft during the tournament.</p>
  <div class="bar" style="left:196px;top:855px;width:310px">Admission: $10.00 per person</div>
  <p class="footer-left">For More Information,<br>contact Tournament Director Dale Haskins:<br><span class="phone">252-381-4926</span></p>
  <p class="footer-right">Hotels Available On-Site<br>Lakeview Suites (252)318-4100<br>Maple Lodge Inn (252)318-6200<br>Harborside Inn (252)318-7300</p>
</section>

</main>
</body>
</html>
```